Vesta Power Web Design

I want a design for a home page that can function as a template for the entire web design. I"m also requesting that the design be adapted as a template for Power Point presentations, as well.

Here"s a brief about our company:

Vesta Power provides its customers with clean, redundant and reliable power. Functioning as a private power producer, Vesta Power owns and operates combined heat and power (CHP) and distributed generation (DG) systems.

Vesta’s management has extensive experience in aerospace turbines engine operation, maintenance, manufacturing and repair. Depending on the customer need, Vesta either builds new generators or refurbish “retired” aerospace turbines into industrial generators. This allows Vesta to deliver generating systems at greatly reduced capital outlays, enabling Vesta Power to offer its customers not only redundant power and grid independence, but significant savings on their energy needs. Vesta’s typical installation size is 500Kws to 3Mws but based upon our customer"s needs, Vesta can site multiple generators to configure systems of larger size.

By using aero derivative turbine engines the company has the flexibility to use the best source of fuel for each site and power requirement. The turbine engine can operate on virtually any combustible fuel. This allows Vesta to utilize the flex fuel practice and operate on either the least expensive fuel available or operate on renewable and biofuels to fulfill the green power requirements mandated by many federal, state and local utility commissions.

Vesta’s market strategy is as follows:

1. Sell reliable and redundant power through a PPAs or lease agreements to industrial or institutional customers with high electrical and thermal needs such as food processors, bio fuel producers, hospitals, casinos, hotels, etc.

2. Lease its systems to customer that “flare gas” as byproducts of their processes such as wastewater treatment facilities, land fills and "stranded gas wells" allowing them to use their waste products to power their facilities and sell excess electricity back to the grid.

3. Partner with other private power producers to provide the turbine generating capacity on a leased basis.
Updates

Please disregard the "turbine logo" that was uploaded as a file and focus only on the "bolt design logo", A (bolt) E.

We like the simple navigation and clean and modern design of sites.

http://www.plumvault.example/

http://www.serviqo.example/

http://www.trylumo.example/

Target Market(s)

Our target markets can be found on the web architecture file I've attached to this submission.

Number of Pages Required

1 page

Requirements
Must have
• The designer must provide a web design and a Power Point template based upon the web design.

• The design must contemplate the web architecture that I""ve included as a file.

```html
<!DOCTYPE html>
<html lang="en">
<head>
<meta charset="utf-8">
<title>Vesta Power – Home Page and Slide Templates</title>
<link href="https://fonts.googleapis.com/css2?family=Arimo:wght@400;700&display=swap" rel="stylesheet">
<style>
  :root{
    --lime:#c8d92a;
    --olive-bar:#54400a;
    --olive-head:#6d7d10;
    --brand-green:#3b9f35;
    --grey-text:#8c8c8c;
    --title-grey:#a99c95;
    --orange:#f5801f;
    --white:#ffffff;
    --frame:#9a9a9a;
    --faint:#e2e2e2;
  }
  *{margin:0;padding:0;box-sizing:border-box}
  html,body{width:866px;height:1200px;overflow:hidden;background:var(--white)}
  body{position:relative;font-family:"Arimo",Arial,sans-serif;color:var(--grey-text)}
  .abs{position:absolute}

  .brand{position:absolute;display:flex;align-items:center;gap:4px;color:var(--brand-green);font-weight:400;white-space:nowrap}
  .brand-dot{border-radius:50%;background:var(--brand-green);flex:none}

  /* nav */
  .main-nav{left:400px;top:21px;display:flex;gap:2px}
  .main-nav a{width:58px;height:57px;background:var(--lime);color:var(--white);font-size:7.3px;text-decoration:none;text-align:center;display:flex;align-items:center;justify-content:center;line-height:1.05;text-transform:uppercase}

  /* hero */
  .hero{left:23px;top:97px;width:820px;height:167px;background:radial-gradient(ellipse at 60% 100%,#ffffff 40%,#eef1ee 75%,#ffffff 100%)}
  .hero-photo{left:126px;top:16px;width:326px;height:151px;background:radial-gradient(ellipse at 40% 120%,#4d73a6 0%,#7e9ab8 35%,#bfcad4 55%,rgba(255,255,255,0) 72%),radial-gradient(ellipse at 75% 40%,#3f7a22 0%,#e0b08f 30%,rgba(255,255,255,0) 50%)}
  .hero-title{left:499px;top:133px;font-size:15.5px;color:var(--olive-head);font-weight:400}
  .hero-copy{left:499px;top:155px;width:222px;font-size:7.6px;line-height:13px;color:#6f6f6f;text-align:justify}
  .btn{left:500px;top:207px;width:87px;height:22px;border-radius:11px;background:linear-gradient(#f9962f,var(--orange));color:var(--white);font-size:8px;display:flex;align-items:center;justify-content:center;text-transform:uppercase;box-shadow:0 3px 4px rgba(0,0,0,.15)}

  /* features */
  .feature{position:absolute;top:273px;width:190px;height:100px}
  .feature h2{position:absolute;left:2px;top:2px;font-size:14.5px;font-weight:400;color:var(--title-grey)}
  .feature svg{position:absolute;left:0;top:32px}
  .feature p{position:absolute;left:71px;top:36px;width:107px;font-size:7px;line-height:11.5px;text-align:justify}
  .read-more{position:absolute;left:124px;top:78px;font-size:7px;color:var(--lime);display:flex;align-items:center;gap:4px}
  .read-more i{width:9px;height:9px;border-radius:50%;background:#3c3c3c;display:inline-block;position:relative}
  .read-more i::after{content:"";position:absolute;left:3px;top:2.3px;border-left:4px solid #fff;border-top:2.2px solid transparent;border-bottom:2.2px solid transparent}

  /* sitemap footer */
  .sitemap{left:23px;top:385px;width:820px;height:127px;background:var(--lime)}
  .sitemap-col{position:absolute;top:12px}
  .sitemap-col h3{font-size:14.5px;font-weight:400;color:var(--white);margin-bottom:8px;white-space:nowrap}
  .sitemap-col li{list-style:none;font-size:8.4px;color:var(--white);height:15.5px;padding-left:9px;position:relative;white-space:nowrap}
  .sitemap-col li::before{content:"";position:absolute;left:0;top:1px;border-left:4px solid #eef3a6;border-top:2.5px solid transparent;border-bottom:2.5px solid transparent}
  .bulb{left:626px;top:32px;width:87px;height:51px;border-radius:50% 45% 45% 50%/55% 50% 50% 45%;background:radial-gradient(circle at 65% 45%,#3e7a2a 0%,#8fb4d0 45%,#5b6066 80%)}
  .legal-bar{left:23px;top:512px;width:820px;height:27px;background:var(--olive-bar);font-size:7.3px;color:var(--lime)}
  .legal-bar span{position:absolute;top:10px;white-space:nowrap}
  .legal-bar .copy{color:var(--white);font-size:8.4px;top:9px}

  /* slides */
  .slide{position:absolute;width:400px;height:300px;border:1px solid var(--frame);overflow:hidden;background:var(--white)}
  .photo-earth{position:absolute;border-radius:50% 50% 0 0/100% 100% 0 0;background:radial-gradient(ellipse at 50% 100%,#6b8f5a 0%,#4b6fa4 40%,#a5b7c9 75%,#dfe6ec 100%)}
  .photo-hand{position:absolute;border-radius:40% 40% 30% 30%;background:radial-gradient(ellipse at 55% 25%,#2f6b1d 0%,#4f8b2c 30%,#e6b796 55%,#d19b78 100%)}
  .band{position:absolute;background:var(--lime)}
  .ghost-name{position:absolute;font-size:40px;color:var(--faint);white-space:nowrap;line-height:1}
</style>
</head>
<body>

<!-- Home page -->
<header>
  <div class="brand" style="left:160px;top:50px;font-size:15px"><span class="brand-dot" style="width:9px;height:9px"></span>Vesta Power</div>
  <nav class="abs main-nav">
    <a href="#">About<br>Vesta</a>
    <a href="#">CHP</a>
    <a href="#">Stranded<br>Gas</a>
    <a href="#">Resources</a>
    <a href="#">Partner<br>&amp; Supplier</a>
    <a href="#">Contact<br>Us</a>
  </nav>
</header>

<section class="abs hero">
  <div class="abs hero-photo" role="img" aria-label="Hands holding a young green plant in soil above the curve of planet Earth"></div>
</section>
<h1 class="abs hero-title">Lorem ipsum dolor sit amet.</h1>
<p class="abs hero-copy">Lorem ipsum dolor sit amet, consectetur adipiscing elit. Cras blandit ullamcorper erat, ac dictum augue egestas sit amet. Maecenas neque nisl,</p>
<a class="abs btn">View About Us</a>

<section class="feature" style="left:158px">
  <h2>What is CHP</h2>
  <svg width="52" height="46" viewBox="0 0 52 46" aria-hidden="true">
    <path d="M4 20 L26 3 L48 20" fill="none" stroke="#2f9a35" stroke-width="4" stroke-linejoin="round"/>
    <rect x="10" y="18" width="32" height="25" rx="3" fill="#7cc242"/>
    <path d="M26 24 C34 26 34 36 26 39 C18 36 18 26 26 24Z" fill="#fff"/>
  </svg>
  <p>Lorem ipsum dolor sit amet, consectetur adipiscing elit. Donec a velit eros,</p>
  <span class="read-more"><i></i>Read More</span>
</section>

<section class="feature" style="left:364px">
  <h2>Stranded Gas</h2>
  <svg width="44" height="46" viewBox="0 0 44 46" aria-hidden="true">
    <circle cx="19" cy="27" r="16" fill="none" stroke="#2f9a35" stroke-width="3.5"/>
    <ellipse cx="19" cy="27" rx="7" ry="14" fill="none" stroke="#2f9a35" stroke-width="2"/>
    <line x1="4" y1="27" x2="34" y2="27" stroke="#2f9a35" stroke-width="2"/>
    <path d="M28 14 C30 4 38 2 42 2 C42 8 38 15 28 14Z" fill="#7cc242"/>
  </svg>
  <p>Lorem ipsum dolor sit amet, consectetur adipiscing elit. Donec a velit eros,</p>
  <span class="read-more"><i></i>Read More</span>
</section>

<section class="feature" style="left:567px">
  <h2>Resources</h2>
  <svg width="44" height="46" viewBox="0 0 44 46" aria-hidden="true">
    <line x1="28" y1="8" x2="28" y2="44" stroke="#2f9a35" stroke-width="2.5"/>
    <ellipse cx="28" cy="6" rx="3" ry="5" fill="#7cc242"/>
    <ellipse cx="21" cy="17" rx="4" ry="8" transform="rotate(-35 21 17)" fill="#2f9a35"/>
    <ellipse cx="35" cy="17" rx="4" ry="8" transform="rotate(35 35 17)" fill="#2f9a35"/>
    <ellipse cx="21" cy="28" rx="4" ry="8" transform="rotate(-35 21 28)" fill="#2f9a35"/>
    <ellipse cx="35" cy="28" rx="4" ry="8" transform="rotate(35 35 28)" fill="#2f9a35"/>
    <ellipse cx="21" cy="38" rx="4" ry="7" transform="rotate(-35 21 38)" fill="#2f9a35"/>
    <ellipse cx="35" cy="38" rx="4" ry="7" transform="rotate(35 35 38)" fill="#2f9a35"/>
  </svg>
  <p>Lorem ipsum dolor sit amet, consectetur adipiscing elit. Donec a velit eros,</p>
  <span class="read-more" style="top:76px"><i></i>Read More</span>
</section>

<footer>
  <div class="abs sitemap">
    <div class="sitemap-col" style="left:138px"><h3>CHP</h3><ul><li>What is CHP?</li><li>Benefits</li><li>Energy Security</li><li>Markets</li></ul></div>
    <div class="sitemap-col" style="left:246px"><h3>Stranded Gas</h3><ul><li>Benefits</li><li>Energy Security</li><li>Markets</li></ul></div>
    <div class="sitemap-col" style="left:372px"><h3>Resources</h3><ul><li>Grid Office</li><li>Air Board</li><li>Gulf Coast</li><li>Application Center</li><li>Etc</li></ul></div>
    <div class="sitemap-col" style="left:492px"><h3>Partner &amp; Supplies</h3><ul><li>Hale &amp; Morrow (help)</li><li>Lorem Ipsum</li><li>Dolor Ipsum</li></ul></div>
    <div class="abs bulb" role="img" aria-label="Light bulb containing a green tree and meadow under blue sky"></div>
  </div>
  <div class="abs legal-bar">
    <span style="left:135px">Texas CHP Critical Infrastructure legislation</span>
    <span style="left:297px">|</span>
    <span style="left:317px">Is your business a good candidate for CHP</span>
    <span style="left:481px">|</span>
    <span style="left:503px">CHP Calculator</span>
    <span class="copy" style="left:589px">Copyright 2010. Vesta Power</span>
  </div>
</footer>

<!-- Slide templates -->
<div class="slide" style="left:21px;top:561px">
  <div class="photo-earth" style="left:44px;top:200px;width:320px;height:85px" role="img" aria-label="Curve of planet Earth seen from space"></div>
  <div class="photo-hand" style="left:260px;top:124px;width:139px;height:161px" role="img" aria-label="Hand holding a young green plant in soil"></div>
  <div class="brand" style="left:136px;top:115px;font-size:18px"><span class="brand-dot" style="width:10px;height:10px"></span>Vesta Power</div>
  <div class="band" style="left:0;top:285px;width:400px;height:15px"></div>
</div>

<div class="slide" style="left:438px;top:563px">
  <div class="brand" style="left:18px;top:38px;font-size:11px"><span class="brand-dot" style="width:7px;height:7px"></span>Vesta Power</div>
  <div class="ghost-name" style="left:270px;top:160px">Vesta Power</div>
  <div class="photo-earth" style="left:0;top:215px;width:121px;height:70px;border-radius:0 100% 0 0/0 100% 0 0" role="img" aria-label="Curve of planet Earth seen from space"></div>
  <div class="photo-hand" style="left:0;top:132px;width:78px;height:100px" role="img" aria-label="Hand holding a young green plant in soil"></div>
  <div class="band" style="left:0;top:284px;width:400px;height:16px"></div>
  <div class="abs" style="left:357px;top:282px;width:21px;height:18px;background:var(--olive-bar)"></div>
</div>

<div class="slide" style="left:17px;top:882px">
  <div class="band" style="left:0;top:0;width:60px;height:300px"></div>
  <div class="photo-hand" style="left:0;top:90px;width:86px;height:104px" role="img" aria-label="Hand holding a young green plant in soil"></div>
  <div class="brand" style="left:94px;top:132px;font-size:9px"><span class="brand-dot" style="width:6px;height:6px"></span>Vesta Power</div>
  <div class="photo-earth" style="left:277px;top:222px;width:160px;height:120px;border-radius:50%" role="img" aria-label="Planet Earth seen from space"></div>
</div>

<div class="slide" style="left:441px;top:882px">
  <div class="band" style="left:0;top:102px;width:400px;height:104px"></div>
  <div class="photo-earth" style="left:105px;top:155px;width:194px;height:51px" role="img" aria-label="Curve of planet Earth seen from space"></div>
  <div class="photo-hand" style="left:0;top:84px;width:76px;height:97px" role="img" aria-label="Hand holding a young green plant in soil"></div>
  <div class="brand" style="left:165px;top:237px;font-size:10px"><span class="brand-dot" style="width:6px;height:6px"></span>Vesta Power</div>
</div>

</body>
</html>
```